Summer Sale Graphics for Social Media

I want to create 11 social media graphics (new Instagram size 4:5 (1080 x 1350 pixels) focusing on our Summer Sale Graphics, using any of the pics attached. Use the attached pics, NO RANDOM STOCK PHOTOGRAPHY. For the color scheme of the graphics, they should all be complementary to the product colors in the photos.
You can add any of the photos attached but none are required. You can do some of the graphics in all text. I mainly need BOLD text that says one of the headlines (11 total) SEE ATTACHED WORD DOCUMENT for the headlines to use.

```html
<!DOCTYPE html>
<html lang="en">
<head>
<meta charset="utf-8">
<title>Summer Sale Social Graphics</title>
<link href="https://fonts.googleapis.com/css2?family=Bebas+Neue&display=swap" rel="stylesheet">
<style>
  :root {
    --board: #a4a4a4;
    --plum: #874a80;
    --plum-deep: #6f3a6c;
    --plum-soft: #a5789b;
    --magenta: #b8478f;
    --red: #e9383b;
    --yellow: #f6b81f;
    --green: #2e5d4c;
    --blue: #4f63c4;
    --paper: #f3f2f2;
    --white: #ffffff;
    --ink-dark: #2a2a2a;
  }
  * { box-sizing: border-box; margin: 0; padding: 0; }
  html, body { width: 1200px; height: 904px; overflow: hidden; background: var(--board); }
  body { position: relative; font-family: "Bebas Neue", "Oswald", sans-serif; color: var(--white); }

  .post { position: absolute; overflow: hidden; }
  .post--plum { background: var(--plum); }
  .post--paper { background: linear-gradient(180deg, #ffffff 0%, var(--paper) 60%, #e9e7e8 100%); }

  .photo { position: absolute; }
  .photo--model { background: linear-gradient(160deg, #8b5a52 0%, #c9a79c 35%, #e9e2e4 55%, #3a2a2e 85%); }
  .photo--products { background: linear-gradient(180deg, rgba(255,255,255,0) 0%, #ece9ec 30%, #dcd6dc 100%); border-radius: 4px; }
  .fade-left { position: absolute; inset: 0; background: linear-gradient(90deg, var(--plum) 0%, var(--plum) 35%, rgba(135,74,128,0.55) 62%, rgba(135,74,128,0.15) 100%); }
  .fade-bottom { position: absolute; inset: 0; background: linear-gradient(0deg, rgba(135,74,128,0.85) 0%, rgba(135,74,128,0.1) 45%); }
  .veil { position: absolute; inset: 0; background: rgba(135,74,128,0.78); }

  .text { position: absolute; line-height: 0.9; text-transform: uppercase; letter-spacing: 0.2px; }
  .center { text-align: center; left: 0; right: 0; }
  .vertical { writing-mode: vertical-rl; transform: rotate(180deg); white-space: nowrap; }

  .frame { position: absolute; border: 1.5px solid var(--white); }
  .red-bar { position: absolute; background: var(--red); color: var(--white); text-align: center; line-height: 1; }

  .badge { position: absolute; font-size: 10px; line-height: 1; padding: 3px 6px 2px; white-space: nowrap; }
  .badge--white { background: var(--white); color: var(--plum-deep); }
  .badge--green { background: var(--green); color: var(--white); }
  .badge--red { background: var(--red); color: var(--white); }
  .badge--blue { background: var(--blue); color: var(--white); }
  .badge--plum { background: var(--plum); color: var(--white); }
  .badge--dark { background: #2c2c2c; color: var(--white); line-height: 1.05; }
</style>
</head>
<body>

<!-- Hero: Your summer body won't wait -->
<section class="post post--plum" style="left:35px;top:30px;width:444px;height:556px;">
  <div class="photo photo--model" role="img" aria-label="Smiling woman in a white crop sweater holding a supplement bottle in a kitchen" style="left:180px;top:0;width:264px;height:556px;"></div>
  <div class="fade-left"></div>
  <div class="photo photo--products" role="img" aria-label="Two supplement bottles on the counter" style="left:252px;top:432px;width:110px;height:96px;"></div>
  <h1 class="text" style="left:26px;top:28px;font-size:57px;line-height:0.92;">Your<br>summer<br>body won’t<br>wait</h1>
  <div class="frame" style="left:28px;top:247px;width:163px;height:194px;"></div>
  <div class="text" style="left:38px;top:255px;font-size:100px;line-height:0.86;">Sale<br>now!</div>
  <div class="badge badge--white" style="left:28px;top:486px;font-size:20px;padding:4px 8px 2px;">Up to $15 off</div>
</section>

<!-- Final countdown -->
<section class="post post--paper" style="left:490px;top:30px;width:217px;height:271px;">
  <div class="text center" style="top:18px;font-size:18px;color:var(--magenta);">Final countdown to</div>
  <div class="text center" style="top:33px;font-size:48px;color:var(--magenta);">Summer</div>
  <div class="red-bar" style="left:34px;top:77px;width:149px;height:36px;font-size:40px;padding-top:1px;">Sale now!</div>
  <div class="photo photo--products" role="img" aria-label="Row of four supplement bottles" style="left:14px;top:128px;width:190px;height:110px;"></div>
  <div class="badge badge--green" style="left:74px;top:249px;">Up to $15 off</div>
</section>

<!-- Detox, burn fat -->
<section class="post post--plum" style="left:723px;top:30px;width:217px;height:271px;">
  <div class="photo photo--model" role="img" aria-label="Woman in a white crop sweater pointing at supplements on a counter" style="left:60px;top:0;width:157px;height:271px;"></div>
  <div class="fade-left"></div>
  <div class="photo photo--products" role="img" aria-label="Full line of supplement bottles on the counter" style="left:70px;top:175px;width:140px;height:78px;opacity:0.8;"></div>
  <div class="text" style="left:8px;top:10px;font-size:19px;line-height:0.92;">Detox, burn fat,<br>and turn heads<br>this summer</div>
  <div class="text vertical" style="left:7px;top:74px;font-size:64px;line-height:0.8;color:var(--yellow);">Sale now!</div>
  <div class="badge badge--dark" style="left:170px;top:242px;font-size:10px;">Up to<br>$15 off</div>
</section>

<!-- Slim waist -->
<section class="post post--paper" style="left:954px;top:30px;width:217px;height:271px;">
  <div class="text center" style="top:16px;font-size:23px;line-height:0.92;color:var(--green);">Slim waist. Flat<br>tummy. More<br>energy. Let’s go!</div>
  <div class="red-bar" style="left:34px;top:84px;width:149px;height:35px;font-size:40px;padding-top:1px;">Sale now!</div>
  <div class="photo photo--products" role="img" aria-label="Row of four supplement bottles" style="left:12px;top:128px;width:193px;height:110px;"></div>
  <div class="badge badge--green" style="left:79px;top:249px;">Up to $15 off</div>
</section>

<!-- Biggest sale of the year -->
<section class="post post--plum" style="left:490px;top:316px;width:217px;height:272px;">
  <div class="photo photo--model" role="img" aria-label="Woman in a brown mesh top holding three bottles by a pool table" style="left:90px;top:0;width:127px;height:272px;"></div>
  <div class="fade-left"></div>
  <div class="text" style="left:9px;top:22px;font-size:23px;line-height:0.93;">Summer’s here.<br>And we’re<br>having the</div>
  <div class="text" style="left:9px;top:99px;font-size:44px;line-height:0.86;color:var(--yellow);">Biggest<br>sale</div>
  <div class="text" style="left:9px;top:180px;font-size:24px;color:var(--yellow);">Of the year</div>
  <div class="badge badge--white" style="left:9px;top:248px;">Up to $15 off</div>
</section>

<!-- One summer to slay -->
<section class="post post--paper" style="left:723px;top:316px;width:217px;height:272px;">
  <div class="text center" style="top:20px;font-size:27px;color:var(--magenta);">One sale. One body.</div>
  <div class="text center" style="top:44px;font-size:44px;line-height:0.84;color:var(--red);">One summer<br>to slay</div>
  <div class="photo photo--products" role="img" aria-label="Four supplement bottles side by side" style="left:10px;top:146px;width:197px;height:100px;"></div>
  <div class="badge badge--red" style="left:75px;top:246px;">Up to $15 off</div>
</section>

<!-- Limited-time summer sale -->
<section class="post post--plum" style="left:954px;top:316px;width:217px;height:272px;">
  <div class="photo photo--model" role="img" aria-label="Close portrait of a smiling woman" style="left:80px;top:60px;width:137px;height:212px;"></div>
  <div class="veil"></div>
  <div class="text center" style="top:14px;font-size:26px;">Limited-time</div>
  <div class="text center" style="top:42px;font-size:58px;line-height:0.88;">Summer<br>sale</div>
  <div style="position:absolute;left:63px;top:161px;width:91px;height:1.5px;background:var(--white);"></div>
  <div class="text center" style="top:175px;font-size:27px;line-height:0.95;">Snatch your<br>supplements now!</div>
  <div class="badge badge--blue" style="left:75px;top:244px;">Up to $15 off</div>
</section>

<!-- Get snatched for summer -->
<section class="post post--plum" style="left:263px;top:600px;width:216px;height:271px;">
  <div class="photo photo--model" role="img" aria-label="Woman in a white crop sweater gesturing toward supplements on a counter" style="left:80px;top:0;width:136px;height:271px;"></div>
  <div class="fade-left"></div>
  <div class="photo photo--products" role="img" aria-label="Full line of supplement bottles on the counter" style="left:84px;top:185px;width:132px;height:70px;opacity:0.8;"></div>
  <div class="text" style="left:8px;top:10px;font-size:19px;line-height:0.92;">Get snatched<br>for summer</div>
  <div class="text vertical" style="left:9px;top:52px;font-size:19px;">Supplements on</div>
  <div class="text vertical" style="left:28px;top:50px;font-size:66px;line-height:0.8;">Sale now!</div>
  <div class="badge badge--plum" style="left:140px;top:250px;">Up to $15 off</div>
</section>

<!-- Summer isn't waiting -->
<section class="post post--plum" style="left:490px;top:600px;width:217px;height:271px;">
  <div class="photo photo--model" role="img" aria-label="Woman in a white crop sweater holding a bottle in a kitchen" style="left:95px;top:0;width:122px;height:271px;"></div>
  <div class="fade-left"></div>
  <div class="photo photo--products" role="img" aria-label="Two supplement bottles on the counter" style="left:120px;top:212px;width:70px;height:54px;"></div>
  <div class="text" style="left:11px;top:14px;font-size:25px;line-height:0.93;">Summer<br>isn’t waiting<br>neither<br>should you</div>
  <div class="frame" style="left:12px;top:117px;width:75px;height:95px;"></div>
  <div class="text" style="left:17px;top:121px;font-size:47px;line-height:0.88;">Sale<br>now!</div>
  <div class="badge badge--white" style="left:12px;top:240px;">Up to $15 off</div>
</section>

<!-- Hurry -->
<section class="post post--plum" style="left:723px;top:600px;width:217px;height:271px;">
  <div class="photo photo--model" role="img" aria-label="Faded photo of a woman behind the supplement line" style="left:40px;top:0;width:137px;height:271px;"></div>
  <div class="veil"></div>
  <div class="text center" style="top:72px;font-size:72px;color:var(--yellow);">Hurry!</div>
  <div class="text center" style="top:139px;font-size:27px;line-height:0.96;">Our summer slim<br>down sale is on<br>don’t miss it!</div>
  <div class="text center" style="top:255px;font-size:10px;">Up to $15 off</div>
</section>

<!-- Sale, your summer body starts here -->
<section class="post post--plum" style="left:954px;top:600px;width:217px;height:271px;">
  <div class="photo photo--model" role="img" aria-label="Woman in a brown mesh top holding three bottles by a pool table" style="left:100px;top:0;width:117px;height:271px;"></div>
  <div class="fade-left"></div>
  <div class="text" style="left:9px;top:12px;font-size:88px;line-height:0.84;">Sale</div>
  <div class="text" style="left:9px;top:86px;font-size:27px;line-height:0.99;">Your<br>summer<br>body<br>starts<br>here</div>
  <div class="badge badge--blue" style="left:10px;top:246px;">Up to $15 off</div>
</section>

</body>
</html>
```